Wordpress Design Project

We are a Computer / Information Technology Company that will focus on the after-hours technical support for Home and Businesses.

I'm looking to have the home page as a static page with a links to blog, about us.

www.rkwidget.com.au is my web site.

Please do not chage uploaded logo's, do not copy current logo on website use uploaded files only, thanks.
Updates

Project Deadline Extended
Reason: No idea how this was posted with only 2 days!!

Cheers

Marcus

Project Deadline Extended
Reason: I have asked for some changes from designers.

Target Market(s)

Home and Small office/home office, or SOHO Computer users.

Industry/Entity Type

Computer

Requirements
Should not have
• After hours tech support added to logo.

```html
<!DOCTYPE html>
<html lang="en">
<head>
<meta charset="utf-8">
<title>RK Widget – After Hours Computer Support</title>
<link rel="stylesheet" href="https://fonts.googleapis.com/css2?family=Ubuntu:wght@400;500&family=Marcellus+SC&family=Arimo:wght@400;700&display=swap">
<style>
:root{
  --blue:#0a74c9;
  --blue-dark:#0a4f9a;
  --blue-light:#1e9be6;
  --navy:#0d2a52;
  --tab-dark:#2b2b2b;
  --page:#f6f7f9;
  --text:#5d5d5d;
  --title:#0d3d78;
  --link:#0a5cb8;
}
*{margin:0;padding:0;box-sizing:border-box}
html,body{width:885px;height:1200px;overflow:hidden;background:var(--page)}
body{font-family:"Arimo",Arial,sans-serif}
.page{position:relative;width:996px;height:1350px;transform:scale(.8886);transform-origin:0 0;background:var(--page)}
.abs{position:absolute}

/* header */
.header{left:0;top:0;width:996px;height:132px;background:linear-gradient(#fff,#e9ebee);border-top:6px solid var(--blue-dark)}
.brand{left:24px;top:38px;display:flex;align-items:center;gap:14px}
.brand-dot{width:56px;height:56px;border-radius:50%;background:var(--blue)}
.brand-name{font-family:"Ubuntu",sans-serif;font-weight:500;font-size:34px;color:var(--blue)}
.follow{left:740px;top:30px;font-family:"Ubuntu",sans-serif;font-size:14px;color:var(--blue)}
.social{top:22px;width:28px;height:28px;border-radius:50%;background:radial-gradient(circle at 40% 35%,#6cc3f5,#1274c7);box-shadow:0 2px 3px rgba(0,0,0,.25)}
.nav{top:102px;height:30px;width:80px;border-radius:8px 8px 0 0;background:var(--tab-dark);color:#fff;font-family:"Ubuntu",sans-serif;font-size:12px;text-align:center;line-height:28px}
.nav.active{background:linear-gradient(var(--blue-light),var(--blue))}

/* banner */
.banner-frame{left:20px;top:132px;width:966px;height:225px;border:3px solid var(--navy);background:#fff}
.banner-photo{left:432px;top:136px;width:552px;height:218px;background:linear-gradient(90deg,#d8dde3,#9aa6b2 40%,#3a3f47 70%,#cfd5dc)}
.banner-panel{left:6px;top:154px;width:427px;height:186px;background:linear-gradient(var(--blue-light),var(--blue-dark));color:#fff;font-family:"Ubuntu",sans-serif;padding:8px 0 0 51px}
.banner-panel h2{font-weight:400;font-size:20px;margin-bottom:4px}
.banner-panel li{list-style:none;font-size:14.5px;line-height:26px;padding-left:16px;position:relative}
.banner-panel li::before{content:"";position:absolute;left:5px;top:9px;border-left:5px solid #fff;border-top:4px solid transparent;border-bottom:4px solid transparent}
.tagline{left:0;top:368px;width:996px;height:36px;background:linear-gradient(var(--blue-light),var(--blue));color:#fff;font-family:"Marcellus SC",serif;font-size:22px;padding-left:18px;line-height:34px}

/* posts */
.post{left:11px;width:700px;height:250px}
.thumb{position:absolute;left:0;top:4px;width:238px;height:162px;border:1px solid #c9ccd0;background:#fff;padding:4px}
.thumb div{width:100%;height:100%}
.post-title{position:absolute;left:248px;top:0;font-family:"Ubuntu",sans-serif;font-weight:400;font-size:20px;color:var(--title)}
.meta{position:absolute;left:248px;top:30px;font-size:12px;color:var(--link)}
.meta span{color:#777}
.excerpt{position:absolute;left:248px;top:55px;width:450px;font-size:11.4px;line-height:18px;color:var(--text);text-align:justify;letter-spacing:.2px}
.excerpt-wide{position:absolute;left:6px;top:182px;width:692px;font-size:11.4px;line-height:18px;color:var(--text);letter-spacing:.2px}
.share{position:absolute;left:9px;top:228px;font-family:"Ubuntu",sans-serif;font-size:12.5px;color:#666;display:flex;align-items:center;gap:4px}
.share i{display:inline-block;width:18px;height:17px;border:1px solid #999;background:#e4e4e4}
.share i:first-child{margin-left:8px}

/* sidebar */
.widget{left:723px;width:260px}
.widget-head{height:28px;background:linear-gradient(var(--blue-light),var(--blue));border-radius:6px 6px 0 0;color:#fff;font-family:"Ubuntu",sans-serif;font-weight:400;font-size:18px;text-align:center;line-height:30px}
.widget-body{background:linear-gradient(var(--page),#e8e8e8);position:relative}
.widget-shadow{height:16px;margin:2px 14px 0;background:radial-gradient(ellipse at top,rgba(0,0,0,.25),transparent 70%)}
.quote{font-size:11.5px;line-height:18px;color:#555;text-align:justify;letter-spacing:.3px;padding:0 10px}
.quote b{color:#333}
.by{text-align:right;font-size:12px;font-weight:700;color:#444;padding-right:14px;margin-bottom:8px}
.btn{background:linear-gradient(var(--blue-light),var(--blue-dark));color:#fff;border-radius:12px;font-size:12px;text-align:center;line-height:22px;letter-spacing:.4px}
.meta-list{list-style:none;padding:16px 0 0 30px;font-family:"Ubuntu",sans-serif;font-size:13.5px;color:#444}
.meta-list li{line-height:24px;position:relative;padding-left:16px}
.meta-list li::before{content:"";position:absolute;left:0;top:8px;border-left:5px solid var(--navy);border-top:4px solid transparent;border-bottom:4px solid transparent}
.field{position:absolute;font-size:11.5px;color:#555;letter-spacing:.5px}
.input{position:absolute;left:92px;width:147px;height:20px;border:1px solid #ccd;border-radius:10px;background:#fff}

/* footer */
.footer{left:0;top:1293px;width:996px;height:57px;background:linear-gradient(var(--blue),var(--blue-light));color:#fff;text-align:center}
.footer nav{padding-top:12px;font-size:12px;word-spacing:2px}
.footer nav span{margin:0 10px}
.footer p{font-size:13px;margin-top:10px}
</style>
</head>
<body>
<div class="page">

  <header class="abs header">
    <div class="abs brand"><span class="brand-dot"></span><span class="brand-name">RK Widget</span></div>
    <div class="abs follow">Follow Us On :</div>
    <span class="abs social" style="left:842px"></span>
    <span class="abs social" style="left:884px"></span>
    <span class="abs social" style="left:928px"></span>
    <a class="abs nav active" style="left:705px">Home</a>
    <a class="abs nav" style="left:789px">Blog</a>
    <a class="abs nav" style="left:873px">Contact US</a>
  </header>

  <section>
    <div class="abs banner-frame"></div>
    <div class="abs banner-photo" role="img" aria-label="Team of business professionals standing and applauding"></div>
    <div class="abs banner-panel">
      <h2>No job is too small Orchard or PC :</h2>
      <ul>
        <li>Home ADSL.</li>
        <li>Wireless.</li>
        <li>Virus removal.</li>
        <li>Panes configuration and installation.</li>
        <li>Orchard configuration and installation.</li>
      </ul>
    </div>
    <div class="abs tagline">After hours computer support for your convenience, with a no fix no fee policy.</div>
  </section>

  <main>
    <article class="abs post" style="top:455px">
      <div class="thumb"><div role="img" aria-label="People working at computers in an office" style="background:linear-gradient(135deg,#1d4f8a,#8fb3d6 50%,#3a6ea8)"></div></div>
      <h3 class="post-title">System image prep</h3>
      <p class="meta">Posted on December 17,2011 <span>By Admin</span></p>
      <p class="excerpt">Lorem Ipsum is simply dummy text of the printing and typesetting industry. Lorem Ipsum has been the industry's standard dummy text ever since the 1500s, when an unknown printer took a galley of type and scrambled it to make a type specimen book. It has survived not only five centuries, but also the leap into electronic typesetting, remaining essentially unchanged. Lorem Ipsum is simply dummy text of the printing and typesetting industry printing and typesetting industry.lorem ipsum.Lorem Ipsum is simply dummy text of the printing an</p>
      <p class="excerpt-wide">Lorem Ipsum is simply dummy text of the printing and typesetting industry. Lorem Ipsum has been the industry's standar text ever since the 1500s,</p>
      <div class="share">Share this : <i></i><i></i><i></i><i></i></div>
    </article>

    <article class="abs post" style="top:726px">
      <div class="thumb"><div role="img" aria-label="Silhouettes of business people at a presentation board" style="background:linear-gradient(135deg,#d6e4f3,#6c94c4 55%,#1e3d6b)"></div></div>
      <h3 class="post-title">System image prep</h3>
      <p class="meta">Posted on December 17,2011 <span>By Admin</span></p>
      <p class="excerpt">Lorem Ipsum is simply dummy text of the printing and typesetting industry. Lorem Ipsum has been the industry's standard dummy text ever since the 1500s, when an unknown printer took a galley of type and scrambled it to make a type specimen book. It has survived not only five centuries, but also the leap into electronic typesetting, remaining essentially unchanged. Lorem Ipsum is simply dummy text of the printing and typesetting industry printing and typesetting industry.lorem ipsum.Lorem Ipsum is simply dummy text of the printing an</p>
      <p class="excerpt-wide">Lorem Ipsum is simply dummy text of the printing and typesetting industry. Lorem Ipsum has been the industry's standar text ever since the 1500s,</p>
      <div class="share">Share this : <i></i><i></i><i></i><i></i></div>
    </article>

    <article class="abs post" style="top:1016px">
      <div class="thumb" style="border:none;background:none"><div role="img" aria-label="Man working on a laptop in an office" style="background:linear-gradient(135deg,#eef2f6,#b9c6d4 50%,#5d6f86)"></div></div>
      <h3 class="post-title">System image prep</h3>
      <p class="meta">Posted on December 17,2011 <span>By Admin</span></p>
      <p class="excerpt">Lorem Ipsum is simply dummy text of the printing and typesetting industry. Lorem Ipsum has been the industry's standard dummy text ever since the 1500s, when an unknown printer took a galley of type and scrambled it to make a type specimen book. It has survived not only five centuries, but also the leap into electronic typesetting, remaining essentially unchanged. Lorem Ipsum is simply dummy text of the printing and typesetting industry printing and typesetting industry.lorem ipsum.Lorem Ipsum is simply dummy text of the printing an</p>
      <p class="excerpt-wide">Lorem Ipsum is simply dummy text of the printing and typesetting industry. Lorem Ipsum has been the industry's standar text ever since the 1500s,</p>
      <div class="share">Share this : <i></i><i></i><i></i><i></i></div>
    </article>
  </main>

  <aside>
    <section class="abs widget" style="top:436px">
      <div class="widget-head">Recent Comments</div>
      <div class="widget-body" style="height:250px;padding-top:20px">
        <p class="quote"><b>“ Lorem Ipsum is simply dummy text of the printing and typesetting industry.</b> Lorem Ipsum has been the industry's standard ”</p>
        <p class="by">Dana Reed</p>
        <p class="quote"><b>“ Lorem Ipsum is simply dummy text of the printing and typesetting industry.</b> Lorem Ipsum has been the industry's standard ”</p>
        <p class="by">Dana Reed</p>
        <div class="abs btn" style="left:167px;top:243px;width:83px">Read more</div>
      </div>
      <div class="widget-shadow" style="margin-top:30px"></div>
    </section>

    <section class="abs widget" style="top:763px">
      <div class="widget-head">Meta</div>
      <ul class="widget-body meta-list" style="height:124px">
        <li>Log in</li>
        <li>Entries RSS</li>
        <li>Comments RSS</li>
        <li>Publisher.org</li>
      </ul>
      <div class="widget-shadow"></div>
    </section>

    <section class="abs widget" style="top:967px">
      <div class="widget-head">Contact Us</div>
      <form class="widget-body" style="height:250px">
        <span class="field" style="left:37px;top:24px">Name :</span><span class="input" style="top:22px"></span>
        <span class="field" style="left:39px;top:50px">Email :</span><span class="input" style="top:48px"></span>
        <span class="field" style="left:33px;top:75px">Mobile :</span><span class="input" style="top:73px"></span>
        <span class="field" style="left:25px;top:101px">Website :</span><span class="input" style="top:99px"></span>
        <span class="field" style="left:20px;top:127px">Message :</span><span class="input" style="top:128px;height:72px;border-radius:8px;width:150px"></span>
        <div class="abs btn" style="left:152px;top:219px;width:92px">Send</div>
      </form>
      <div class="widget-shadow"></div>
    </section>
  </aside>

  <footer class="abs footer">
    <nav>Home<span>|</span>About Us<span>|</span>Services<span>|</span>Blog<span>|</span>Contact Us</nav>
    <p>© 2011 rkwidget.com.au - All rights reserved</p>
  </footer>

</div>
</body>
</html>
```